Occupational Therapy Clinic Advertisement

Create an advertisement for a magazine. Below I have attached my original ad (Ad 2020.pdf) . I want the ad changed and it should be eye catching. I would like a eye catching graphics added in the ad. It should be a graphic image that applies to education. I am attaching a sample graphic image of that I liked from someone elses ad- it should not be the same- it just is there to show what I like. Please use the same words from my original ad.Dimensions: 3.75in x 10.3 in

Target Market(s)

Parents of School aged children

Requirements
Must have
• Must have eye catching Graphic. Colors should be eye catching for a typed magazine.

```html
<!DOCTYPE html>
<html lang="en">
<head>
<meta charset="utf-8">
<title>Bright Path OT Services</title>
<link href="https://fonts.googleapis.com/css2?family=Fredoka:wght@600&family=Ubuntu:wght@400;500;700&display=swap" rel="stylesheet">
<style>
  :root{
    --backdrop:#88898b;
    --paper:#f3f3f4;
    --purple:#7f4fa2;
    --indigo:#3e3a8e;
    --pink:#ef5aa0;
    --orange:#f6a623;
    --ink:#2b2b2b;
    --grey:#6d6d6d;
    --muted:#7a7a7a;
    --silver-light:#ececee;
    --silver-mid:#d3d3d7;
    --lilac:#ddd3e8;
  }
  *{margin:0;padding:0;box-sizing:border-box}
  html,body{width:674px;height:1200px;overflow:hidden;background:var(--backdrop)}
  body{position:relative;font-family:"Ubuntu",sans-serif;color:var(--ink)}
  .ad{position:absolute;left:175px;top:155px;width:324px;height:890px;
    background:radial-gradient(ellipse at 50% 45%,#ffffff 0%,var(--paper) 70%);overflow:hidden}

  .brand{position:absolute;top:20px;left:0;width:100%;text-align:center;
    font-size:38px;line-height:44px;font-weight:500;color:var(--indigo);letter-spacing:-0.5px}
  .brand-sub{position:absolute;top:66px;width:100%;text-align:center;font-size:20px;line-height:24px;
    color:var(--grey);letter-spacing:1.5px}
  .top-phone{position:absolute;top:102px;width:100%;text-align:center;font-size:19px;line-height:22px;
    font-weight:700;letter-spacing:1.2px;display:flex;justify-content:center;align-items:center;gap:6px}
  .top-phone svg{width:18px;height:18px}

  .questions{position:absolute;top:160px;left:10px;width:304px;display:flex;align-items:flex-start}
  .question{text-align:center;font-size:11.5px;line-height:12.6px}
  .question:nth-child(1){width:107px}
  .question:nth-child(2){width:93px;border-left:1px solid #d8d8d8;padding-top:1px;min-height:62px}
  .question:nth-child(3){width:104px;border-left:1px solid #d8d8d8;padding-top:1px;min-height:62px}
  .question b{font-weight:700}

  .illustration{position:absolute;left:48px;top:254px;width:229px;height:453px;
    background:linear-gradient(180deg,var(--silver-light) 0%,var(--silver-mid) 45%,var(--lilac) 100%);
    clip-path:polygon(0 0,100% 0,100% 51%,70% 51%,70% 100%,30% 100%,30% 51%,0 51%)}
  .headline{position:absolute;left:48px;top:309px;width:229px;text-align:center;
    font-family:"Fredoka",sans-serif;font-weight:600;font-size:27px;line-height:31px;
    color:var(--purple);letter-spacing:-0.5px}
  .headline s{color:var(--orange);text-decoration-color:var(--ink);text-decoration-thickness:1px}

  .tab{position:absolute;left:0;width:21px;color:#fff;font-size:12px;font-weight:700;
    writing-mode:vertical-rl;transform:rotate(180deg);display:flex;align-items:center;justify-content:center}
  .tab-evaluate{top:504px;height:93px;background:var(--pink)}
  .tab-treat{top:597px;height:85px;background:var(--purple)}
  .methods{position:absolute;left:31px;top:553px;font-size:12.5px;line-height:13.5px;color:var(--muted)}
  .methods p + p{margin-top:14px}
  .treat-note{position:absolute;left:209px;top:583px;font-size:15px;line-height:17px;font-weight:500}

  .baseline{position:absolute;left:28px;top:707px;width:268px;height:1px;
    background:linear-gradient(90deg,transparent,#b8a77a,transparent)}
  .ages{position:absolute;top:716px;width:100%;display:flex;justify-content:center;align-items:center;
    gap:8px;font-size:15px;line-height:18px;font-weight:700}
  .dots{width:38px;height:14px;background:radial-gradient(circle,var(--pink) 1px,transparent 1.3px) 0 0/4.5px 4.5px}
  .rsa{position:absolute;top:746px;left:20px;width:284px;height:20px;text-align:center;
    font-size:13.5px;font-weight:500;letter-spacing:1px;line-height:20px;
    background:linear-gradient(90deg,transparent,#e4e4e6 20%,#e4e4e6 80%,transparent)}
  .location{position:absolute;top:776px;width:100%;text-align:center;font-size:10px;line-height:12.5px}
  .contact{position:absolute;top:808px;width:100%;text-align:center;font-size:10.5px;line-height:12px}
  .contact .email{font-weight:700;margin-top:2px;display:inline-flex;align-items:center;gap:4px}
  .footer{position:absolute;left:10px;top:851px;width:304px;height:39px;background:var(--purple);
    color:#fff;display:flex;align-items:center;justify-content:center;gap:5px;font-size:12.5px;font-weight:500}
  .footer small{font-size:9px;font-weight:400}
  .footer .num{font-size:14px}
  .footer svg{width:13px;height:13px}
</style>
</head>
<body>
<main class="ad">
  <h1 class="brand">Bright Path</h1>
  <p class="brand-sub">OT Services</p>
  <p class="top-phone">
    <svg viewBox="0 0 24 24" aria-hidden="true"><path fill="#2b2b2b" d="M6.6 10.8c1.4 2.8 3.8 5.1 6.6 6.6l2.2-2.2c.3-.3.7-.4 1-.2 1.1.4 2.3.6 3.6.6.6 0 1 .4 1 1V20c0 .6-.4 1-1 1C10.6 21 3 13.4 3 4c0-.6.4-1 1-1h3.5c.6 0 1 .4 1 1 0 1.3.2 2.5.6 3.6.1.3 0 .7-.2 1z"/></svg>
    (555) 214-0187
  </p>

  <section class="questions">
    <p class="question">Does your<br>child <b>struggle</b><br>with<br><b>Reading/Kriah</b>?</p>
    <p class="question">Knows the<br>information<br>but <b>fails</b><br><b>the test</b>?</p>
    <p class="question">Has <b>difficulty</b><br><b>remembering</b><br>names and<br>dates?</p>
  </section>

  <div class="illustration" role="img" aria-label="Illustration of a silver magnifying glass whose handle is a striped teal, purple and red sharpened pencil"></div>
  <h2 class="headline">Yes Your<br>Child <s>can</s><br>Will Succeed<br>in School!</h2>

  <div class="tab tab-evaluate">We Evaluate</div>
  <div class="tab tab-treat">We Treat</div>
  <div class="methods">
    <p>Using<br>standardized<br>Evaluations</p>
    <p>Using<br>Researched<br>based<br>techniques</p>
  </div>
  <p class="treat-note">We Treat the<br>underlying<br>processing<br>deficits</p>

  <div class="baseline"></div>
  <p class="ages"><span class="dots"></span>Ages : 6-18<span class="dots"></span></p>
  <p class="rsa">Board of Ed OT RSA's accepted</p>
  <p class="location">Located in Borough Park<br>Evaluations done in Borough Park &amp; Staten Island</p>
  <p class="contact">For more information or to be added<br>to our email list, please email:<br>
    <span class="email">&#9993; brightpathot@example.com</span></p>

  <footer class="footer">
    <span>Dena Halberstam <small>OTR/L</small></span>
    <svg viewBox="0 0 24 24" aria-hidden="true"><path fill="#fff" d="M6.6 10.8c1.4 2.8 3.8 5.1 6.6 6.6l2.2-2.2c.3-.3.7-.4 1-.2 1.1.4 2.3.6 3.6.6.6 0 1 .4 1 1V20c0 .6-.4 1-1 1C10.6 21 3 13.4 3 4c0-.6.4-1 1-1h3.5c.6 0 1 .4 1 1 0 1.3.2 2.5.6 3.6.1.3 0 .7-.2 1z"/></svg>
    <span class="num">(555)214-0187</span>
  </footer>
</main>
</body>
</html>
```